New Business Card Design Project

Make a kick ass business card for The Otter Tea Mug, using the designs. I also might like the 2nd place design logo on the back? Maybe all black with that? Not sure. Also, I'm cool with it being on metal, plastic, glass? or whatever for the business card. Maybe shaped like a shark? Let me know what else you need? Would like designs in the next day or so. Thank you.
Target Market(s)
Anyone that is cool
Contact Information for Business Card
Name: Dorian Fenwick
Phone: 317.594.8126
inventor/creator/entrepreneur/owner
www.theottertyeamug.example
social media links
https://www.facebook.com/theottertyeamug
https://twitter.com/otter_brew
https://www.instagram.com/theottertyeamug/
I'll get the Pinterest one soon
Colors
Designer to choose colors to be used in the design.
Requirements
Must have
- The Otter Tea Mug
- www.theottertyeamug.example
- social media tags?
- My logos and picture/photo of wine glass
Nice to have
- Maybe shaped like a wine glass or shark
- I'll let you decide but my same colors from my website would be nice

```html
<!DOCTYPE html>
<html lang="en">
<head>
<meta charset="utf-8">
<title>Otter Tea Mug — Business Card</title>
<link rel="stylesheet" href="https://fonts.googleapis.com/css2?family=Questrial&family=Roboto:wght@400;500&display=swap">
<style>
  :root {
    --page-bg: #e4e4e6;
    --card-white: #ffffff;
    --card-grey: #dcdcde;
    --wine-red: #b01e32;
    --wine-deep: #4a0810;
    --ink: #1d1d1f;
    --logo-grey: #7a7a7c;
    --glass-line: #2a2a2a;
  }
  * { box-sizing: border-box; margin: 0; padding: 0; }
  html, body { width: 1200px; height: 1021px; overflow: hidden; }
  body {
    background: var(--page-bg);
    font-family: "Roboto", Arial, sans-serif;
    color: var(--ink);
    position: relative;
  }
  .card {
    position: absolute;
    top: 143px;
    width: 420px;
    height: 735px;
    background: linear-gradient(180deg, var(--card-white) 0%, #f4f4f5 55%, var(--card-grey) 100%);
    box-shadow: 0 6px 22px rgba(0,0,0,0.18);
    overflow: hidden;
  }
  .card--front { left: 150px; }
  .card--back  { left: 630px; }

  .glass-photo {
    position: absolute;
    left: 30px;
    top: 180px;
    width: 360px;
    height: 555px;
    border-radius: 14px 14px 0 0;
  }
  .card--front .glass-photo {
    background: linear-gradient(180deg, #fbfbfb 0%, #f1f1f1 42%, var(--wine-red) 56%, var(--wine-deep) 80%, #c9c9cb 100%);
  }
  .card--back .glass-photo {
    background: linear-gradient(180deg, #fafafa 0%, #eeeeef 55%, #c8c8ca 85%, #b9b9bb 100%);
  }

  .brand {
    position: absolute;
    top: 78px;
    left: 0;
    width: 100%;
    display: flex;
    align-items: center;
    justify-content: center;
    gap: 14px;
  }
  .brand__dot {
    width: 22px; height: 22px;
    border-radius: 50%;
    background: var(--wine-red);
  }
  .brand__name {
    font-family: "Questrial", Arial, sans-serif;
    font-size: 38px;
    color: var(--logo-grey);
    letter-spacing: 0.5px;
  }

  .contact {
    position: absolute;
    top: 218px;
    left: 0;
    width: 100%;
    text-align: center;
  }
  .contact__name { font-size: 27px; color: var(--wine-red); font-weight: 500; }
  .contact__role { font-size: 20px; line-height: 1.3; margin-top: 6px; }
  .contact__rule {
    width: 36px; height: 3px; background: var(--ink);
    margin: 18px auto 14px;
  }
  .contact__phone { font-size: 28px; color: var(--wine-red); letter-spacing: 1px; }

  .website {
    position: absolute;
    top: 90px;
    left: 0; width: 100%;
    text-align: center;
    font-size: 19px;
    color: var(--ink);
  }
  .website__domain { color: var(--wine-red); }

  .social {
    position: absolute;
    top: 232px;
    left: 92px;
  }
  .social__icons { display: flex; gap: 7px; margin-bottom: 10px; }
  .social__icon {
    width: 22px; height: 22px;
    border-radius: 4px;
    background: var(--wine-red);
  }
  .social__handle { font-size: 19px; line-height: 1.32; }
</style>
</head>
<body>

  <section class="card card--front" aria-label="Business card front">
    <div class="glass-photo" role="img" aria-label="Photo of a wine glass lying on its side, half filled with red wine, with a glass shark figure inside"></div>
    <div class="brand">
      <span class="brand__dot"></span>
      <span class="brand__name">Otter Tea Mug</span>
    </div>
    <div class="contact">
      <p class="contact__name">Dorian Fenwick</p>
      <p class="contact__role">Inventor / Creator<br>Entrepreneur / Owner</p>
      <div class="contact__rule"></div>
      <p class="contact__phone">317.594.8126</p>
    </div>
  </section>

  <section class="card card--back" aria-label="Business card back">
    <p class="website">www.<span class="website__domain">theottertyeamug</span>.example</p>
    <div class="glass-photo" role="img" aria-label="Photo of an empty wine glass with a glass shark figure inside"></div>
    <div class="social">
      <div class="social__icons">
        <span class="social__icon"></span>
        <span class="social__icon"></span>
        <span class="social__icon"></span>
        <span class="social__icon"></span>
      </div>
      <p class="social__handle">/theottertyeamug</p>
      <p class="social__handle">/otter_brew</p>
      <p class="social__handle">/theottertyeamug</p>
      <p class="social__handle">/ottertyeamug</p>
    </div>
  </section>

</body>
</html>
```